Leaf Haven Business Card Design

My E-Commerce store is called Leaf Haven

Website address is - http://www.leafhaven-demo.com.au

I would like a colourful, friendly business with the description in the 'must haves' box incorporated into it
Updates

Please add the following to the business cards; Natural & Organic Products Online Organic Pantry Items Superfoods & Supplements Natural Skincare Eco Friendly Household Products

Industry/Entity Type

Business

Contact Information for Business Card

www.leafhaven-demo.com.au
mira@leafhaven-demo.com.au

Colors
acd037
9bcb3c
cadf82
eaf2ce

Requirements
Must have
• Natural & Organic Eco Products Online.
• Leaf Haven specialises in organic pantry items, superfoods and supplements, organic skincare for you and your family & eco friendly household products.

```html
<!DOCTYPE html>
<html lang="en">
<head>
<meta charset="utf-8">
<title>Leaf Haven Business Card</title>
<link rel="stylesheet" href="https://fonts.googleapis.com/css2?family=Arimo:wght@400;700&display=swap">
<style>
  :root {
    --page-bg: #eef1e6;
    --card-white: #ffffff;
    --lime: #acd037;
    --lime-mid: #9bcb3c;
    --lime-soft: #cadf82;
    --lime-pale: #eaf2ce;
    --lime-deep: #7fa824;
    --text-olive: #5d8418;
    --text-white: #ffffff;
  }
  * { margin: 0; padding: 0; box-sizing: border-box; }
  html, body {
    width: 1200px;
    height: 950px;
    overflow: hidden;
    background: var(--page-bg);
    font-family: "Arimo", Arial, sans-serif;
  }
  .sheet { position: relative; width: 1200px; height: 950px; }
  .card {
    position: absolute;
    left: 250px;
    width: 700px;
    height: 400px;
    overflow: hidden;
    box-shadow: 0 8px 24px rgba(0, 0, 0, 0.16);
  }
  .card-front { top: 50px; background: var(--card-white); }
  .card-back  { top: 500px; }
  .card-art { position: absolute; inset: 0; width: 100%; height: 100%; }

  /* Brand */
  .brand { position: absolute; display: flex; align-items: center; gap: 12px; }
  .brand-dot { width: 28px; height: 28px; border-radius: 50%; flex: none; }
  .brand-name { font-size: 38px; font-weight: 700; letter-spacing: 0.3px; white-space: nowrap; }

  .card-front .brand { left: 48px; top: 160px; }
  .card-front .brand-dot { background: var(--lime); }
  .card-front .brand-name { color: var(--text-olive); }
  .front-tagline {
    position: absolute;
    left: 48px;
    top: 214px;
    width: 290px;
    font-size: 14px;
    line-height: 1.4;
    color: var(--text-olive);
  }

  /* Contact */
  .contact { position: absolute; left: 432px; top: 140px; color: var(--text-white); }
  .person-name { font-size: 24px; font-weight: 700; letter-spacing: 0.5px; }
  .person-role { font-size: 17px; margin-top: 4px; }
  .contact-list { list-style: none; margin-top: 28px; }
  .contact-item {
    display: flex; align-items: center; gap: 9px;
    font-size: 15px; margin-bottom: 10px; white-space: nowrap;
  }
  .contact-icon { width: 15px; height: 15px; flex: none; }

  /* Back */
  .card-back .brand { left: 0; right: 0; top: 56px; justify-content: center; }
  .card-back .brand-dot { background: var(--lime-pale); }
  .card-back .brand-name { color: var(--text-white); }
  .back-description {
    position: absolute;
    left: 80px; right: 80px; top: 128px;
    text-align: center;
    color: var(--text-white);
    font-size: 15px;
    line-height: 1.5;
  }
  .product-list {
    position: absolute;
    left: 110px; right: 90px; top: 218px;
    list-style: none;
    display: grid;
    grid-template-columns: 1fr 1fr;
    column-gap: 24px;
    row-gap: 10px;
    color: var(--text-white);
    font-size: 15px;
  }
  .product-item { display: flex; align-items: center; gap: 10px; white-space: nowrap; }
  .product-item::before {
    content: "";
    width: 8px; height: 8px; border-radius: 50%;
    background: var(--lime-pale);
    flex: none;
  }
  .back-web {
    position: absolute;
    left: 0; right: 0; top: 340px;
    text-align: center;
    color: var(--lime-pale);
    font-size: 16px;
    letter-spacing: 1px;
  }
</style>
</head>
<body>
<main class="sheet">

  <section class="card card-front" aria-label="Business card front">
    <svg class="card-art" viewBox="0 0 700 400" aria-hidden="true">
      <defs>
        <linearGradient id="front-green" x1="0" y1="0" x2="1" y2="1">
          <stop offset="0" stop-color="#acd037"/>
          <stop offset="1" stop-color="#7fa824"/>
        </linearGradient>
      </defs>
      <path d="M 470 0 C 350 50, 320 240, 400 400 L 700 400 L 700 0 Z" fill="#cadf82"/>
      <path d="M 490 0 C 372 52, 345 240, 420 400 L 700 400 L 700 0 Z" fill="#ffffff"/>
      <path d="M 500 0 C 385 55, 358 240, 432 400 L 700 400 L 700 0 Z" fill="url(#front-green)"/>
    </svg>

    <div class="brand">
      <span class="brand-dot"></span>
      <span class="brand-name">Leaf Haven</span>
    </div>
    <p class="front-tagline">Natural &amp; Organic Eco Products Online</p>

    <div class="contact">
      <p class="person-name">Sam Rivers</p>
      <p class="person-role">President</p>
      <ul class="contact-list">
        <li class="contact-item">
          <svg class="contact-icon" viewBox="0 0 16 16" aria-hidden="true">
            <rect x="1" y="3" width="14" height="10" rx="1" fill="#ffffff"/>
            <path d="M1.5 3.5 L8 9 L14.5 3.5" fill="none" stroke="#7fa824" stroke-width="1.4"/>
          </svg>
          <span>mira@leafhaven-demo.com.au</span>
        </li>
        <li class="contact-item">
          <svg class="contact-icon" viewBox="0 0 16 16" aria-hidden="true">
            <circle cx="8" cy="8" r="7" fill="#ffffff"/>
            <path d="M6.5 5 L10.5 8 L6.5 11 Z" fill="#7fa824"/>
          </svg>
          <span>www.leafhaven-demo.com.au</span>
        </li>
      </ul>
    </div>
  </section>

  <section class="card card-back" aria-label="Business card back">
    <svg class="card-art" viewBox="0 0 700 400" aria-hidden="true">
      <defs>
        <linearGradient id="back-green" x1="0" y1="0" x2="1" y2="1">
          <stop offset="0" stop-color="#9bcb3c"/>
          <stop offset="1" stop-color="#7fa824"/>
        </linearGradient>
      </defs>
      <rect width="700" height="400" fill="url(#back-green)"/>
    </svg>

    <div class="brand">
      <span class="brand-dot"></span>
      <span class="brand-name">Leaf Haven</span>
    </div>
    <p class="back-description">Leaf Haven specialises in organic pantry items, superfoods and supplements, organic skincare for you and your family &amp; eco friendly household products.</p>
    <ul class="product-list">
      <li class="product-item">Natural &amp; Organic Products Online</li>
      <li class="product-item">Organic Pantry Items</li>
      <li class="product-item">Superfoods &amp; Supplements</li>
      <li class="product-item">Natural Skincare</li>
      <li class="product-item">Eco Friendly Household Products</li>
    </ul>
    <p class="back-web">www.leafhaven-demo.com.au</p>
  </section>

</main>
</body>
</html>
```